Paper and board wholesaler needs business card design for managers

We need a business card design that incorporates bordo red, white and/ or grey colors. The business card has to have our "KRITEX" logo and our partners paper group logo that we are part of - "VORMA group". Both of the logos should be applied to the business card according to the guidelines for the usage of the logo that have been added in the uploaded files.
The letters (information on the card) should be easily readable, so no "shiny" or "glossy" text.
Besides the two logos, the business card needs to contain information for the respective person:
1) Name, Surname,
2) Job position (e.g. "sales represantative"),
3) E-mail,
4) Phone number,
5) text: "Drukātavas Sēta (KRITEX)" LTD
6) our office address "Riga, Kalnupes street 42".
(also could have) 7) our homepage address "www.kritex.lv"
Holiday season, so have a lot of tasks to take care of and not as much time to check ArtHive as often.
1) Name, Surname, 2) Job position (e.g. "sales represantative"), 3) E-mail, 4) Phone number, 5) text: "Drukātavas Sēta (KRITEX)" LTD 6) our office address "Riga, Kalnupes street 42". (also could have) 7) our homepage address "www.kritex.lv"
- Josefin Sans

```html
<!DOCTYPE html>
<html lang="lv">
<head>
<meta charset="utf-8">
<title>KRITEX business card</title>
<link rel="stylesheet" href="https://fonts.googleapis.com/css2?family=Montserrat:wght@400;500;700&display=swap">
<style>
  :root {
    --bordo: #813136;
    --white: #ffffff;
    --ink: #2b2b2b;
    --rule: #555555;
    --bg-top: #cfcfcf;
    --bg-bottom: #a9a9a9;
  }
  * { margin: 0; padding: 0; box-sizing: border-box; }
  html, body { width: 1200px; height: 815px; overflow: hidden; }
  body {
    background: linear-gradient(180deg, var(--bg-top), var(--bg-bottom));
    font-family: "Montserrat", Arial, sans-serif;
    position: relative;
  }
  .card {
    position: absolute;
    top: 259px;
    width: 520px;
    height: 297px;
    box-shadow: 0 12px 28px rgba(0,0,0,0.28);
  }
  .card--front { left: 40px; background: var(--white); }
  .card--back { left: 640px; background: var(--bordo); color: var(--white); }

  .brand {
    position: absolute;
    display: flex;
    align-items: center;
    gap: 18px;
  }
  .brand__square {
    border: 2px solid currentColor;
    flex: none;
  }
  .brand__name {
    font-weight: 500;
    letter-spacing: 0.75em;
    line-height: 1;
  }
  .card--front .brand { left: 232px; top: 48px; color: var(--bordo); }
  .card--front .brand__square { width: 34px; height: 34px; }
  .card--front .brand__name { font-size: 19px; }

  .partner {
    position: absolute;
    display: flex;
    align-items: center;
    gap: 6px;
    font-size: 11px;
    font-weight: 500;
    letter-spacing: 0.04em;
    line-height: 1;
  }
  .partner__dot {
    width: 9px; height: 9px;
    border-radius: 50%;
    background: currentColor;
    flex: none;
  }
  .card--front .partner { left: 36px; top: 24px; color: var(--bordo); }
  .card--back .partner { right: 24px; bottom: 20px; color: var(--white); }

  .person { position: absolute; left: 36px; top: 138px; }
  .person__name {
    color: var(--bordo);
    font-weight: 700;
    font-size: 22px;
    letter-spacing: 0.02em;
    line-height: 1.1;
  }
  .person__role { color: var(--ink); font-size: 13px; margin-top: 2px; }

  .divider {
    position: absolute;
    left: 36px; right: 30px; top: 196px;
    height: 1px; background: var(--rule);
  }

  .contacts {
    position: absolute; left: 36px; top: 210px;
    list-style: none; font-size: 12.5px; color: var(--ink);
  }
  .contacts li { display: flex; align-items: center; gap: 8px; height: 22px; }
  .contacts svg, .address svg { width: 11px; height: 11px; flex: none; }

  .address {
    position: absolute; right: 30px; top: 214px;
    display: flex; align-items: center; gap: 7px;
    font-size: 12.5px; color: var(--ink);
  }

  .card--back .brand { left: 50%; top: 108px; transform: translateX(-50%); color: var(--white); }
  .card--back .brand__square { width: 50px; height: 50px; }
  .card--back .brand__name { font-size: 27px; margin-right: -0.75em; }
  .legal {
    position: absolute; left: 0; right: 0; top: 218px;
    text-align: center; font-size: 13px; letter-spacing: 0.04em;
  }
</style>
</head>
<body>

<section class="card card--front" aria-label="Business card front">
  <div class="partner">
    <span class="partner__dot"></span>
    <span class="partner__name">VORMA group</span>
  </div>

  <div class="brand">
    <span class="brand__square"></span>
    <span class="brand__name">KRITEX</span>
  </div>

  <div class="person">
    <p class="person__name">MARKS VILKS</p>
    <p class="person__role">Sales Represantative</p>
  </div>

  <div class="divider"></div>

  <ul class="contacts">
    <li>
      <svg viewBox="0 0 12 12" aria-hidden="true"><path fill="#813136" d="M2.5 1l2 2.3-1 1.3c.7 1.5 1.9 2.7 3.4 3.4l1.3-1 2.3 2-1.3 1.8C5 10.5 1.5 7 .7 2.3z"/></svg>
      123-555-0147
    </li>
    <li>
      <svg viewBox="0 0 12 12" aria-hidden="true"><rect x="0.5" y="2" width="11" height="8" fill="#813136"/><path d="M0.5 2.5L6 6.5l5.5-4" fill="none" stroke="#fff" stroke-width="1"/></svg>
      info@kritex.lv
    </li>
    <li>
      <svg viewBox="0 0 12 12" aria-hidden="true"><circle cx="6" cy="6" r="5.5" fill="#813136"/><path d="M.5 6h11M6 .5v11M2 3h8M2 9h8" stroke="#fff" stroke-width=".7" fill="none"/></svg>
      www.kritex.lv
    </li>
  </ul>

  <p class="address">
    Riga, Kalnupes street 42
    <svg viewBox="0 0 12 12" aria-hidden="true"><path fill="#813136" d="M6 0a4 4 0 0 1 4 4c0 3-4 8-4 8S2 7 2 4a4 4 0 0 1 4-4z"/><circle cx="6" cy="4" r="1.4" fill="#fff"/></svg>
  </p>
</section>

<section class="card card--back" aria-label="Business card back">
  <div class="brand">
    <span class="brand__square"></span>
    <span class="brand__name">KRITEX</span>
  </div>
  <p class="legal">Drukātavas Sēta (KRITEX)" LTD</p>
  <div class="partner">
    <span class="partner__dot"></span>
    <span class="partner__name">VORMA group</span>
  </div>
</section>

</body>
</html>
```